Design for Poster ad for Cheerleading Gym

I need someone to design a poster type ad for my Cheerleading gym. The ad will be displayed in our local mall during the holiday season. I have attached photo, but have a higher resolution available. I have also attached the spec sheet. I would like the photo with the text "Soar" over it, at the top of the ad. The background to fade from a light color (blue?) at the top to black at the bottom. Text at the bottom to be:
logo
Tumbling Classes/ Cheer Classes/ Competitive Teams
842 Velmont Rd., Torrance
ridgeflipacademy.com
phone number

Target Market(s)

Teenagers and children ages 10-18 , parents of children ages 6-10 years

Industry/Entity Type

Gym

Requirements
Must have
• The photo attached. A catch word like "Soar" at the top. The text at the bottom should include logo, Tumbling Classes/ Cheer Classes/ Competitive Teams, 842 Velmont Rd., Torrance, ridgeflipacademy.com, (424)731-2694
Nice to have
• light to dark background
Should not have
• Not a lot of text

```html
<!DOCTYPE html>
<html lang="en">
<head>
<meta charset="utf-8">
<title>Soar – Ridge Flip Academy</title>
<link rel="stylesheet" href="https://fonts.googleapis.com/css2?family=Great+Vibes&family=Questrial&family=Stardos+Stencil:wght@700&display=swap">
<style>
  :root {
    --sky-top: #bcd2ef;
    --sky-mid: #8da2bc;
    --dusk: #4e6078;
    --night: #05223a;
    --script-teal: #1b5470;
    --ring-deep: #0a7fbf;
    --ring-pale: #c9e9fa;
    --disc-fill: #dfeaf7;
    --tagline: #b9cfe8;
    --contact: #d5e3f3;
    --logo-ink: #1d5f80;
  }
  * { margin: 0; padding: 0; box-sizing: border-box; }
  html, body { width: 960px; height: 1200px; overflow: hidden; }
  body { background: var(--night); }
  .poster {
    position: relative;
    width: 960px;
    height: 1200px;
    overflow: hidden;
    background: linear-gradient(180deg, var(--sky-top) 0%, var(--sky-mid) 28%, var(--dusk) 55%, var(--night) 100%);
  }
  .headline {
    position: absolute;
    top: 8px;
    left: 0;
    width: 100%;
    text-align: center;
    font-family: "Great Vibes", cursive;
    font-size: 178px;
    line-height: 1;
    color: var(--script-teal);
  }
  .circles {
    position: absolute;
    top: 0;
    left: 0;
  }
  .brand-name {
    position: absolute;
    left: 530px;
    top: 680px;
    width: 400px;
    text-align: center;
    font-family: "Questrial", sans-serif;
    font-size: 34px;
    line-height: 1.1;
    color: var(--logo-ink);
  }
  .footer {
    position: absolute;
    left: 0;
    width: 100%;
    text-align: center;
  }
  .offerings {
    top: 972px;
    font-family: "Stardos Stencil", sans-serif;
    font-weight: 700;
    font-size: 31px;
    letter-spacing: 0.3px;
    color: var(--tagline);
  }
  .address {
    top: 1030px;
    font-family: "Questrial", sans-serif;
    font-size: 23px;
    color: var(--contact);
  }
  .phone {
    top: 1076px;
    font-family: "Questrial", sans-serif;
    font-size: 48px;
    color: var(--contact);
  }
  .website {
    top: 1140px;
    font-family: "Questrial", sans-serif;
    font-size: 29px;
    color: var(--contact);
  }
</style>
</head>
<body>
<main class="poster">
  <h1 class="headline">Soar</h1>

  <svg class="circles" width="960" height="1200" viewBox="0 0 960 1200">
    <defs>
      <linearGradient id="ring-gradient" x1="0.8" y1="0" x2="0.2" y2="1">
        <stop offset="0" stop-color="var(--ring-deep)"/>
        <stop offset="0.5" stop-color="#2ea4dc"/>
        <stop offset="1" stop-color="var(--ring-pale)"/>
      </linearGradient>
      <radialGradient id="athlete-tone" cx="0.5" cy="0.45" r="0.55">
        <stop offset="0" stop-color="#3a2a24"/>
        <stop offset="0.55" stop-color="#8a5a3e"/>
        <stop offset="1" stop-color="#c58f68" stop-opacity="0"/>
      </radialGradient>
      <clipPath id="big-disc-clip">
        <circle cx="400" cy="578" r="332"/>
      </clipPath>
    </defs>

    <g class="feature-circle">
      <circle cx="376" cy="564" r="364" fill="url(#ring-gradient)"/>
      <circle cx="400" cy="578" r="332" fill="var(--disc-fill)"/>
      <g clip-path="url(#big-disc-clip)">
        <ellipse class="athlete-photo" cx="380" cy="575" rx="150" ry="300"
                 fill="url(#athlete-tone)" role="img"
                 aria-label="Photo of a cheerleader in black athletic wear mid back-tuck, upside down in the air"/>
      </g>
    </g>

    <g class="brand-circle">
      <circle cx="730" cy="716" r="220" fill="url(#ring-gradient)"/>
      <circle cx="728" cy="712" r="204" fill="var(--disc-fill)"/>
    </g>
  </svg>

  <p class="brand-name">Ridge Flip Academy</p>

  <p class="footer offerings">TUMBLING CLASSES - CHEER CLASSES - COMPETITIVE TEAMS</p>
  <p class="footer address">842 VELMONT RD., TORRANCE</p>
  <p class="footer phone">424-731-2694</p>
  <p class="footer website">ridgeflipacademy.com</p>
</main>
</body>
</html>
```